Stationary or Corporate Identity package for small Software Development Company

I have a logo and am looking for letterhead, envelope, and possibly business card design. Letterhead and envelope can use all images from the attached business card or open to other ideas that can incorporate the logo. Looking for colorful design to grab attention. Also wanting a more Professional look and less whimsical with maybe a little on the bolder side (maybe more of the masculine side?) Definitely a more modern look over a boring traditional look.

Target Market(s)

Clients are IT Recruiters and IT/Software Staffing and Consulting companies

Industry/Entity Type

Computer Software

Font styles to use
Sans Serif

Requirements
Must have
• Must have the logo, and places for address information, phone number, email, and website information. Colors should coordinate with logo.
Nice to have
• I like the look where there is a semi-transparent abstract image or part of the logo that sort of swooshes in from the left side of the paper. This is not necessary if other good ideas come to mind. Would like a little bit of color to the stationary and envelope, not just a header/footer type with just the logo and a colored separation line.

```html
<!DOCTYPE html>
<html lang="en">
<head>
<meta charset="utf-8">
<title>Vantrix Stationery</title>
<link href="https://fonts.googleapis.com/css2?family=Open+Sans:wght@400;600;700;800&family=Tinos&display=swap" rel="stylesheet">
<style>
  :root{
    --bg:#eceeef;
    --paper:#ffffff;
    --ink:#2b2b2b;
    --muted:#777a7d;
    --card-dark:#3a3b3d;
    --blue:#1a7fa6;
    --navy:#1d5aa8;
    --red:#e0262c;
    --green:#3bab3f;
    --orange:#f4a21f;
    --mark:#e85a1e;
    --sans:'Open Sans', Arial, sans-serif;
    --serif:'Tinos', 'Times New Roman', serif;
  }
  *{box-sizing:border-box;margin:0;padding:0}
  html,body{width:1200px;height:795px;overflow:hidden;background:var(--bg)}
  body{position:relative;font-family:var(--sans);color:var(--ink)}
  .sheet{position:absolute;background:var(--paper);box-shadow:0 2px 8px rgba(0,0,0,.12);overflow:hidden}
  .stripe{position:absolute;left:0;right:0;bottom:0;height:5px;
    background:linear-gradient(90deg,var(--blue) 0 62%,var(--navy) 62% 72%,var(--red) 72% 81%,var(--green) 81% 90%,var(--orange) 90% 100%)}
  .brand{position:absolute;display:flex;align-items:center;gap:6px}
  .brand-dot{border-radius:50%;background:var(--mark);flex:none}
  .brand-text{display:flex;flex-direction:column;line-height:1}
  .brand-name{font-weight:800;color:var(--ink);letter-spacing:-.3px}
  .brand-tag{font-weight:400;color:var(--muted);margin-top:2px}
  .faint-circle{position:absolute;border-radius:50%;background:var(--mark);opacity:.12}
  .footer-line{position:absolute;font-size:5.5px;color:var(--muted);line-height:1.5}

  /* letterhead */
  .letterhead{left:40px;top:40px;width:380px;height:537px}
  .letterhead .brand{right:30px;top:30px}
  .letterhead .brand-dot{width:22px;height:22px}
  .letterhead .brand-name{font-size:16px}
  .letterhead .brand-tag{font-size:6px}
  .letter{position:absolute;left:40px;top:90px;width:300px;font-family:var(--serif);font-size:7.5px;line-height:1.5;color:#555}
  .letter p{margin-bottom:8px}
  .letterhead .faint-circle{width:150px;height:150px;left:170px;top:330px}
  .letterhead .footer-line{left:30px;bottom:14px}

  /* folder */
  .folder{left:450px;top:40px;width:380px;height:537px}
  .folder .brand{left:40px;bottom:60px}
  .folder .brand-dot{width:44px;height:44px}
  .folder .brand-name{font-size:30px}
  .folder .brand-tag{font-size:9px}

  /* business cards */
  .card{width:300px;height:160px}
  .card-front{left:860px;top:40px}
  .card-front .brand{left:50%;top:50%;transform:translate(-50%,-50%)}
  .card-front .brand-dot{width:26px;height:26px}
  .card-front .brand-name{font-size:20px}
  .card-front .brand-tag{font-size:6.5px}
  .card-back{left:860px;top:220px;display:flex}
  .card-back .side{width:40%;position:relative}
  .card-back .side .brand{left:14px;top:58px}
  .card-back .side .brand-dot{width:16px;height:16px}
  .card-back .side .brand-name{font-size:13px}
  .card-back .side .brand-tag{font-size:4.5px}
  .card-back .panel{width:60%;background:var(--card-dark);color:#e6e6e6;padding:20px 16px;font-size:7px;line-height:1.6}
  .card-back .panel .person{font-size:10px;font-weight:700;color:#fff}
  .card-back .panel .role{color:#b9b9b9;margin-bottom:10px}

  /* envelopes */
  .envelope{width:300px;height:150px}
  .env-front{left:860px;top:410px}
  .env-front .brand{left:18px;top:16px}
  .env-front .brand-dot{width:18px;height:18px}
  .env-front .brand-name{font-size:14px}
  .env-front .brand-tag{font-size:5px}
  .env-front .faint-circle{width:90px;height:90px;left:180px;top:40px}
  .env-front .footer-line{left:18px;bottom:12px;font-size:5px}
  .env-back{left:860px;top:590px}
  .env-back svg{position:absolute;left:0;top:0}
  .env-back .seal{position:absolute;left:140px;top:48px;width:20px;height:20px;border-radius:50%;background:var(--mark)}
</style>
</head>
<body>

<section class="sheet letterhead">
  <div class="brand">
    <span class="brand-dot"></span>
    <div class="brand-text"><span class="brand-name">Vantrix</span><span class="brand-tag">Software Development</span></div>
  </div>
  <div class="letter">
    <p>Riverton, HL 40418<br>June 25, 2017</p>
    <p>Ms. Laura Bennett<br>Harbor Fellowship<br>22 Lakeview Road<br>Marston, HL 40522</p>
    <p>Dear Ms. Bennett:</p>
    <p>The Harbor Fellowship has always stood on the horizon for me. Ever since I decided to pursue software, I have wanted to take part in your program. From the moment I learned of your work, I felt the fellowship would give me the tools and guidance to grow and to give back.</p>
    <p>I believe my skills, experience, and goals make me a strong candidate for your program.</p>
    <p>Thank you very much for considering me for the Harbor Fellowship. I am looking forward to hearing from you.</p>
    <p>Sincerely,<br><br>Laura<br>(555) 555-0142</p>
    <p>Enclosure</p>
  </div>
  <div class="faint-circle" role="img" aria-label="Faint brand circle decoration"></div>
  <div class="footer-line">Northgate Software | Address: 48 Elm Street, Riverton, County Hale | Tel: (555) 010 4821 | Fax: (555) 010 4822<br>info@vantrix.dev | www.vantrix.dev</div>
  <div class="stripe"></div>
</section>

<section class="sheet folder">
  <div class="brand">
    <span class="brand-dot"></span>
    <div class="brand-text"><span class="brand-name">Vantrix</span><span class="brand-tag">Software Development</span></div>
  </div>
  <div class="stripe"></div>
</section>

<section class="sheet card card-front">
  <div class="brand">
    <span class="brand-dot"></span>
    <div class="brand-text"><span class="brand-name">Vantrix</span><span class="brand-tag">Software Development</span></div>
  </div>
</section>

<section class="sheet card card-back">
  <div class="side">
    <div class="brand">
      <span class="brand-dot"></span>
      <div class="brand-text"><span class="brand-name">Vantrix</span><span class="brand-tag">Software Development</span></div>
    </div>
  </div>
  <div class="panel">
    <div class="person">Laura Bennett</div>
    <div class="role">Managing Director</div>
    <div>48 Elm Street, Riverton</div>
    <div>T: (555) 010 4821</div>
    <div>info@vantrix.dev</div>
    <div>www.vantrix.dev</div>
  </div>
</section>

<section class="sheet envelope env-front">
  <div class="brand">
    <span class="brand-dot"></span>
    <div class="brand-text"><span class="brand-name">Vantrix</span><span class="brand-tag">Software Development</span></div>
  </div>
  <div class="faint-circle" role="img" aria-label="Faint brand circle decoration"></div>
  <div class="footer-line">Northgate Software | Address: 48 Elm Street, Riverton, County Hale | Tel: (555) 010 4821<br>info@vantrix.dev | www.vantrix.dev</div>
  <div class="stripe"></div>
</section>

<section class="sheet envelope env-back">
  <svg width="300" height="150" viewBox="0 0 300 150" aria-hidden="true">
    <polyline points="0,0 12,58 288,58 300,0" fill="none" stroke="#dcdcdc" stroke-width="1"/>
  </svg>
  <div class="seal"></div>
  <div class="stripe"></div>
</section>

</body>
</html>
```